Application Dashboard Skin - Non coded theme only

We are looking for a website color theme/look feel for a new .net dashboard application we are building. Target audience who will be using this are E and C level professionals. We are looking for the following:

Images of optional color themes for our existing dashboard. You can access a temporary version with no styling here: http://demo.plexaroni-app.com:99/ . Application built in telerik and highcharts.

We are not looking for finished code or application skins. Our development team will take your final design (with specific colors/images/etc. provided) and apply it to the final beta version of the application.

Design considerations:
We are open to creative ideas, but please know that preference will be given to professional designs with emphasis on a consistent brand look/feel. Designs and colors should be focused on quickly identifying and processing the data.

Multiple submissions welcome.

-Quorventa team

Target Market(s)

IT / Insurance

Industry/Entity Type

Building

Number of Pages Required

3 page

Requirements
Must have
• Application Dashboard link for design: http://demo.plexaroni-app.com:99/

```html
<!DOCTYPE html>
<html lang="en">
<head>
<meta charset="utf-8">
<title>Claimvista – Performance Dashboard</title>
<link rel="stylesheet" href="https://fonts.googleapis.com/css2?family=Roboto:wght@300;400;500&display=swap">
<style>
:root{
  --orange:#f5821f;
  --blue:#2196f3;
  --bar-blue:#1e90ff;
  --navy:#0f4594;
  --ink:#0f2340;
  --light-bar:#72bcf7;
  --text:#333;
  --muted:#666;
  --line:#d9d9d9;
  --row-alt:#ebebeb;
}
*{box-sizing:border-box;margin:0;padding:0}
html,body{width:1174px;height:1200px;overflow:hidden}
body{font-family:"Roboto",Arial,sans-serif;color:var(--text);
  background:linear-gradient(115deg,#f4f4f4 0%,#fff 30%,#ececec 55%,#fafafa 75%,#eeeeee 100%);position:relative}
.site-header{position:absolute;left:0;top:0;width:1174px;height:110px;
  background:linear-gradient(#ffffff,#ececec);border-bottom:1px solid #d4d4d4}
.brand{position:absolute;left:172px;top:32px;display:flex;align-items:center;gap:10px}
.brand-name{font-size:36px;font-weight:400;color:#222;letter-spacing:-.5px}
.brand-dot{width:26px;height:26px;border-radius:50%;background:var(--orange)}
.brand-tag{position:absolute;left:352px;top:70px;font-size:12px;color:#333}
.main-nav{position:absolute;top:26px;left:0;width:100%}
.nav-item{position:absolute;width:140px;margin-left:-70px;text-align:center;font-size:14px;color:#444}
.nav-item svg{display:block;margin:0 auto 8px;width:26px;height:26px}
.panel{position:absolute;background:#fff;border:1px solid var(--line)}
.panel-head{height:40px;display:flex;align-items:center;justify-content:space-between;padding:0 10px 0 18px;color:#fff;font-size:15px}
.head-orange{background:var(--orange)}
.head-blue{background:var(--blue);height:41px;padding-left:30px;font-size:18px}
.select{border:1px solid rgba(255,255,255,.85);padding:5px 28px 5px 10px;font-size:12.5px;position:relative}
.select::after{content:"";position:absolute;right:11px;top:9px;width:6px;height:6px;border-right:1.5px solid currentColor;border-bottom:1.5px solid currentColor;transform:rotate(45deg)}
.chart-title{position:absolute;width:100%;text-align:center}
.accuracy-title{top:58px;font-size:18px;color:#222}
.accuracy-sub{top:86px;font-size:12px;color:#666}
.impact-head{height:44px;background:#eeeeee;display:flex;align-items:center;justify-content:space-between;padding:0 17px 0 22px;font-size:14.5px;color:#222}
.impact-head .select{border-color:#ccc;color:#666;background:#fff}
.tabs{display:flex;height:34px;background:var(--navy)}
.tab{color:#fff;font-size:12.5px;display:flex;align-items:center;justify-content:center;border-right:1px solid #3a66ad}
.tab.is-active{background:#fff;color:var(--navy)}
.sub-title{position:absolute;width:100%;text-align:center;color:var(--navy);font-size:15px}
.kpi-lead{height:33px;background:var(--ink);color:#fff;display:flex;align-items:center;font-size:14px;padding-left:30px}
.kpi-lead span:last-child{position:absolute;left:209px}
.kpi-list{list-style:none;margin-top:4px}
.kpi-list li{height:26.2px;display:flex;align-items:center;font-size:11px;color:#333;padding-left:30px;position:relative}
.kpi-list li:nth-child(even){background:var(--row-alt)}
.kpi-list li span:last-child{position:absolute;left:209px}
.donut-label{position:absolute;width:100%;text-align:center;font-size:16px;color:#222}
.legend{position:absolute;width:100%;display:flex;justify-content:center;gap:24px;font-size:11px;color:var(--navy)}
.legend i{display:inline-block;width:8px;height:8px;border-radius:50%;margin-right:8px}
.site-footer{position:absolute;left:0;top:1146px;width:1174px;height:54px;background:#dcdcdc;font-size:12px;color:#666;padding:20px 0 0 182px}
.menu{position:absolute;width:24px;height:12px;border-top:2px solid #777;border-bottom:2px solid #777}
.menu::after{content:"";position:absolute;left:0;right:0;top:3px;border-top:2px solid #777}
.charts{position:absolute;left:0;top:0;pointer-events:none;font-family:"Roboto",Arial,sans-serif}
</style>
</head>
<body>

<header class="site-header">
  <div class="brand"><span class="brand-name">Claimvista</span><span class="brand-dot"></span></div>
  <div class="brand-tag">Performance Insight</div>
  <nav class="main-nav">
    <div class="nav-item" style="left:570px">
      <svg viewBox="0 0 26 26" fill="none" stroke="#f5821f" stroke-width="2"><rect x="3" y="8" width="13" height="15" rx="1"/><rect x="10" y="3" width="13" height="15" rx="1"/></svg>Accuracy Results</div>
    <div class="nav-item" style="left:710px">
      <svg viewBox="0 0 26 26" fill="#f5821f"><path d="M23 3c-6 0-11 3-14 9l5 5c6-3 9-8 9-14z"/><path d="M8 13l-5 1 3-5 5-1zM13 18l-1 5 5-3 1-5z"/><path d="M6 17l3 3-5 3z"/></svg>Processor Accuracy</div>
    <div class="nav-item" style="left:840px">
      <svg viewBox="0 0 26 26" fill="#f5821f"><circle cx="13" cy="8" r="6"/><path d="M2 25c0-7 5-10 11-10s11 3 11 10z"/></svg>Manage Users</div>
    <div class="nav-item" style="left:934px">
      <svg viewBox="0 0 26 26"><circle cx="13" cy="13" r="8" fill="none" stroke="#f5821f" stroke-width="6" stroke-dasharray="3.2 3.1"/><circle cx="13" cy="13" r="7" fill="#f5821f"/><circle cx="13" cy="13" r="3" fill="#fff"/></svg>Settings</div>
  </nav>
</header>

<section class="panel" style="left:172px;top:166px;width:538px;height:317px">
  <div class="panel-head head-orange"><span>Accuracy Results</span><span class="select">End to End</span></div>
  <div class="chart-title accuracy-title">YTD Overall Accuracy</div>
  <div class="chart-title accuracy-sub">Click the bar to view YTD Details for the specific region</div>
  <div class="menu" style="left:499px;top:52px"></div>
</section>

<section class="panel" style="left:170px;top:497px;width:540px;height:629px">
  <div class="impact-head"><span>Error Impact for June 2016</span><span class="select">All Regions</span></div>
  <div class="tabs">
    <div class="tab is-active" style="width:100px">All Errors</div>
    <div class="tab" style="width:90px">Providers</div>
    <div class="tab" style="width:93px">Employers</div>
    <div class="tab" style="width:97px;border-right:0">LineOfBusiness</div>
  </div>
  <div class="sub-title" style="top:91px;left:-14px">Top 10 Error Reasons</div>
  <div class="menu" style="left:497px;top:97px"></div>
  <div class="sub-title" style="top:362px;left:-10px">Top 10 Error Reasons - Financial Impact</div>
  <div class="menu" style="left:500px;top:367px"></div>
</section>

<section class="panel" style="left:721px;top:166px;width:294px;height:457px">
  <div class="panel-head head-blue"><span>KPI's</span><span class="select">All Regions</span></div>
  <div class="kpi-lead"><span>Overall YTD Accuracy</span><span>97.41%</span></div>
  <ul class="kpi-list">
    <li><span>Claims Audited:</span><span>4859</span></li>
    <li><span>Avg. Claims Audited per day:</span><span>6.7</span></li>
    <li><span>Errors Found:</span><span>2147</span></li>
    <li><span>Financial Impact:</span><span>$1,462,139</span></li>
    <li><span>Total Claims Posted:</span><span>17,773,591</span></li>
    <li><span>Total Encounter Claims:</span><span>93,984,586</span></li>
    <li><span>Total Auto Adjudication Claim:</span><span>920,918</span></li>
    <li><span>Total Adjustment Claim Count:</span><span>920,918</span></li>
    <li><span>Total Denied Claim Count:</span><span>133,523</span></li>
    <li><span>Total Dollars Paid:</span><span>$5,669,835,044</span></li>
    <li><span>Auto Adjudication Rate:</span><span>$0.052</span></li>
    <li><span>Adjustment Rate:</span><span>1.345%</span></li>
    <li><span>Denial Rate:</span><span>0.751%</span></li>
  </ul>
</section>

<section class="panel" style="left:721px;top:633px;width:294px;height:493px">
  <div class="menu" style="left:257px;top:20px"></div>
  <div class="donut-label" style="top:180px">Paid vs Denied</div>
  <div class="legend" style="top:208px"><span><i style="background:#0f4594"></i>Denied- 0.7%</span><span><i style="background:#2196f3"></i>Paid- 99.3%</span></div>
  <div class="donut-label" style="top:414px">Paid vs Encounter</div>
  <div class="legend" style="top:441px"><span><i style="background:#0f4594"></i>Denied- 84.1%</span><span><i style="background:#2196f3"></i>Paid- 15.9%</span></div>
</section>

<svg class="charts" width="1174" height="1200" viewBox="0 0 1174 1200">
  <!-- accuracy bar chart -->
  <g font-size="11" fill="#444" text-anchor="end">
    <g stroke="#e3e3e3"><line x1="232" y1="302" x2="694" y2="302"/><line x1="232" y1="332" x2="694" y2="332"/><line x1="232" y1="361" x2="694" y2="361"/><line x1="232" y1="391" x2="694" y2="391"/><line x1="232" y1="420" x2="694" y2="420"/><line x1="232" y1="450" x2="694" y2="450"/></g>
    <text x="227" y="306">100</text><text x="227" y="336">97.5</text><text x="227" y="365">95</text><text x="227" y="395">92.5</text><text x="227" y="424">90</text><text x="227" y="454">87.5</text>
  </g>
  <rect x="255" y="329" width="63" height="124" fill="var(--bar-blue)"/>
  <rect x="346" y="298" width="62" height="155" fill="var(--navy)"/>
  <rect x="430" y="342" width="63" height="111" fill="var(--bar-blue)"/>
  <rect x="523" y="326" width="63" height="127" fill="var(--navy)"/>
  <rect x="628" y="366" width="62" height="87" fill="var(--bar-blue)"/>
  <g font-size="28" fill="#fff" fill-opacity=".4" text-anchor="middle">
    <text transform="translate(297 404) rotate(-90)">97.7%</text>
    <text transform="translate(387 401) rotate(-90)">98.5%</text>
    <text transform="translate(472 401) rotate(-90)">96.8%</text>
    <text transform="translate(565 404) rotate(-90)">97.7%</text>
    <text transform="translate(670 410) rotate(-90)">94.9%</text>
  </g>
  <g font-size="12" fill="#444" text-anchor="middle">
    <text x="284" y="471">Colorado</text><text x="375" y="471">Georgia</text><text x="460" y="471">Hawaii</text><text x="555" y="471">MidAtlantic</text><text x="659" y="471">Northwest</text>
  </g>

  <!-- count chart -->
  <g stroke="#e0e0e0"><line x1="440" y1="622" x2="440" y2="812"/><line x1="511" y1="622" x2="511" y2="812"/><line x1="582" y1="622" x2="582" y2="812"/><line x1="653" y1="622" x2="653" y2="812"/></g>
  <line x1="369" y1="622" x2="369" y2="812" stroke="#ccc"/>
  <g font-size="10.5" fill="#555" text-anchor="end">
    <text x="335" y="633">Incorrect Contract</text><text x="335" y="651">Claim Paid Incorrectly</text><text x="335" y="670">Not a Halvern benefit Bill</text><text x="335" y="689">Incorrect Co-Pay</text><text x="335" y="708">Copay Amount not correct</text><text x="335" y="727">Did Not Follow Desk</text><text x="335" y="746">Did Not Follow PNP</text><text x="335" y="765">Claim Denied in Error</text><text x="335" y="784">Unkown</text><text x="335" y="803">Denied Incorrectly</text>
  </g>
  <g stroke="#ccc"><line x1="352" y1="629" x2="366" y2="629"/><line x1="352" y1="648" x2="366" y2="648"/><line x1="352" y1="667" x2="366" y2="667"/><line x1="352" y1="686" x2="366" y2="686"/><line x1="352" y1="705" x2="366" y2="705"/><line x1="352" y1="724" x2="366" y2="724"/><line x1="352" y1="743" x2="366" y2="743"/><line x1="352" y1="762" x2="366" y2="762"/><line x1="352" y1="781" x2="366" y2="781"/><line x1="352" y1="800" x2="366" y2="800"/></g>
  <rect x="369" y="620" width="261" height="18" fill="var(--orange)"/>
  <rect x="369" y="639" width="181" height="18" fill="var(--bar-blue)"/>
  <rect x="369" y="658" width="161" height="18" fill="var(--orange)"/>
  <rect x="369" y="677" width="152" height="18" fill="var(--bar-blue)"/>
  <rect x="369" y="696" width="131" height="18" fill="var(--orange)"/>
  <rect x="369" y="715" width="131" height="18" fill="var(--bar-blue)"/>
  <rect x="369" y="734" width="124" height="18" fill="var(--orange)"/>
  <rect x="369" y="753" width="100" height="18" fill="var(--bar-blue)"/>
  <rect x="369" y="772" width="100" height="18" fill="var(--orange)"/>
  <rect x="369" y="791" width="75" height="18" fill="var(--bar-blue)"/>
  <g font-size="10.5" fill="#555">
    <text x="635" y="632">35</text><text x="556" y="651">26</text><text x="535" y="670">24</text><text x="526" y="689">23</text><text x="505" y="709">20</text><text x="505" y="727">20</text><text x="498" y="746">19</text><text x="474" y="766">14</text><text x="474" y="784">14</text><text x="448" y="805">12</text>
  </g>
  <g font-size="11" fill="#444" text-anchor="middle">
    <text x="369" y="830">0</text><text x="422" y="830">10</text><text x="499" y="830">20</text><text x="575" y="830">30</text><text x="653" y="830">40</text>
  </g>
  <text x="500" y="848" font-size="12" fill="var(--blue)" text-anchor="middle">Count</text>

  <!-- financial chart -->
  <g stroke="#e0e0e0"><line x1="430" y1="896" x2="430" y2="1088"/><line x1="490" y1="896" x2="490" y2="1088"/><line x1="550" y1="896" x2="550" y2="1088"/><line x1="604" y1="896" x2="604" y2="1088"/><line x1="655" y1="896" x2="655" y2="1088"/></g>
  <line x1="367" y1="896" x2="367" y2="1088" stroke="#ccc"/>
  <g font-size="10.5" fill="#555" text-anchor="end">
    <text x="338" y="910">Incorrect Contract</text><text x="338" y="929">Claim Paid Incorrectly</text><text x="338" y="948">Not a Halvern benefit Bill</text><text x="338" y="967">Incorrect Co-Pay</text><text x="338" y="986">Copay Amount not correct</text><text x="338" y="1005">Did Not Follow Desk</text><text x="338" y="1024">Did Not Follow PNP</text><text x="338" y="1043">Claim Denied in Error</text><text x="338" y="1062">Unkown</text><text x="338" y="1082">Denied Incorrectly</text>
  </g>
  <g fill="var(--light-bar)">
    <rect x="406" y="896" width="255" height="14"/>
    <rect x="535" y="915" width="79" height="14"/>
    <rect x="615" y="953" width="16" height="14"/>
    <rect x="540" y="1010" width="81" height="14"/>
    <rect x="616" y="1029" width="7" height="14"/>
    <rect x="604" y="1067" width="7" height="14"/>
  </g>
  <g font-size="9" fill="var(--navy)" letter-spacing="-.3">
    <text x="412" y="906">$-65155.67</text><text x="616" y="906">$ 12510.63</text>
    <text x="463" y="925">$-26915.92</text><text x="574" y="925">$2919.39</text>
    <text x="565" y="944">$ -245</text><text x="606" y="944">$ 0</text>
    <text x="565" y="963">$ -3898.21</text><text x="642" y="963">$693.01</text>
    <text x="590" y="982">$ -295</text><text x="626" y="982">$10</text>
    <text x="590" y="1001">$0</text><text x="610" y="1001">$0</text>
    <text x="438" y="1020">$-29341.33</text><text x="565" y="1020">$10390.26</text>
    <text x="590" y="1039">$6509.7</text>
    <text x="590" y="1058">$0</text><text x="615" y="1058">$331.1</text>
    <text x="565" y="1078">$1805.56</text>
  </g>
  <g font-size="11" fill="#444" text-anchor="middle">
    <text x="373" y="1100">-80k</text><text x="432" y="1100">-60k</text><text x="490" y="1100">-40k</text><text x="550" y="1100">-20k</text><text x="604" y="1100">0k</text><text x="655" y="1100">20k</text>
  </g>
  <text x="496" y="1118" font-size="12" fill="var(--blue)" text-anchor="middle">Amount</text>

  <!-- donuts -->
  <circle cx="871" cy="729" r="59.5" fill="none" stroke="var(--blue)" stroke-width="39"/>
  <circle cx="871" cy="729" r="59.5" fill="none" stroke="var(--navy)" stroke-width="39" stroke-dasharray="14 360" transform="rotate(-60 871 729)"/>
  <circle cx="869" cy="958" r="59.5" fill="none" stroke="var(--navy)" stroke-width="39"/>
  <circle cx="869" cy="958" r="59.5" fill="none" stroke="var(--blue)" stroke-width="39" stroke-dasharray="10 364" transform="rotate(-58 869 958)"/>
</svg>

<footer class="site-footer">© 2016 Company Name &nbsp;All right reserved &nbsp;Term of Use</footer>

</body>
</html>
```